We want a hot New Design for our IT company Web Site

We have a basic website with some general information and lots of mostly words and generic pictures we want to make it look and feel a lot more modern and slick. The site needs to work on mobile devices as well as desktops.

Target Market(s)

Business customers

Industry/Entity Type

It Company

Coding

Coded - Design and coding required

Number of Pages Required

5+ page

Requirements
Must have
• Sleek new Design making it look and feel more modern and less boring
Nice to have
• If it can have a better flow to it rather then have the std Drop down menus it has now.

```html
<!DOCTYPE html>
<html lang="en">
<head>
<meta charset="utf-8">
<title>K &amp; R Solutions Group</title>
<link href="https://fonts.googleapis.com/css2?family=Open+Sans:wght@400;600;700;800&display=swap" rel="stylesheet">
<style>
:root{
  --blue:#1a73c9;
  --blue-dark:#0f5aa3;
  --ink:#222;
  --charcoal:#2d2f33;
  --charcoal-2:#3a3d42;
  --grey-bg:#e9eaec;
  --text:#555;
  --muted:#9aa0a6;
  --white:#fff;
}
*{margin:0;padding:0;box-sizing:border-box}
html,body{width:1200px;height:2356px;overflow:hidden;background:var(--white);font-family:"Open Sans",Arial,sans-serif;color:var(--text)}
.page{position:relative;width:1200px;height:2356px}

/* header + hero */
.hero{position:absolute;left:0;top:0;width:1200px;height:660px;background:radial-gradient(ellipse at 70% 45%,#4e6478 0%,#26323e 45%,#12171d 100%)}
.hero-art{position:absolute;left:560px;top:60px;width:600px;height:560px;background:radial-gradient(circle at 50% 45%,rgba(170,200,225,.35),rgba(20,30,40,0) 70%)}
.topbar{position:absolute;left:0;top:0;width:1200px;height:48px;background:rgba(20,22,26,.85)}
.brand{position:absolute;left:110px;top:0;width:280px;height:120px;background:var(--white);display:flex;align-items:center;justify-content:center;gap:12px;box-shadow:0 4px 10px rgba(0,0,0,.3)}
.brand-mark{width:30px;height:30px;background:var(--blue)}
.brand-name{font-weight:800;font-size:22px;color:var(--blue);letter-spacing:.5px}
.phone{position:absolute;right:110px;top:12px;color:var(--white);font-size:16px;font-weight:600;display:flex;align-items:center;gap:8px}
.social{display:flex;gap:8px}
.social span{width:26px;height:26px;background:#5b5f66;display:block}
.hero .social{position:absolute;right:110px;top:66px}
.hero-title{position:absolute;left:120px;top:290px;color:var(--white);font-size:34px;font-weight:700;line-height:1.3}
.dots{position:absolute;left:128px;top:476px;display:flex;gap:8px}
.dots i{width:12px;height:12px;border-radius:50%;background:#8ab4e0;display:block}
.dots i:first-child{background:var(--blue)}

/* nav */
.nav{position:absolute;left:0;top:660px;width:1200px;height:80px;background:var(--blue);display:flex;justify-content:center;gap:34px}
.nav a{color:var(--white);text-decoration:none;font-size:15px;font-weight:600;display:flex;flex-direction:column;align-items:center;justify-content:center;gap:6px}
.nav svg{width:22px;height:22px;fill:var(--white)}

/* about */
.about{position:absolute;left:0;top:740px;width:1200px;height:300px;background:var(--grey-bg);text-align:center}
.about-mark{width:36px;height:24px;background:var(--blue);margin:48px auto 10px}
.about h2{font-size:30px;font-weight:700;color:var(--ink)}
.about h2 b{color:var(--blue);font-weight:700}
.about p{width:960px;margin:16px auto 0;font-size:13px;line-height:1.6;color:#666}
.read-more{display:inline-block;margin-top:18px;font-size:14px;font-weight:600;color:var(--ink)}

/* services */
.services{position:absolute;left:0;top:1040px;width:1200px;height:410px}
.services svg.bg{position:absolute;left:0;top:0}
.services-intro{position:absolute;left:0;top:60px;width:1200px;text-align:center;color:var(--white);font-size:14px;letter-spacing:.3px}
.service-list{position:absolute;left:150px;top:120px;width:900px;display:flex;justify-content:space-between}
.service{width:190px;text-align:center;color:var(--white);font-size:15px;font-weight:700;line-height:1.35}
.service .ring{width:120px;height:120px;border-radius:50%;border:4px solid var(--white);margin:0 auto 20px;display:flex;align-items:center;justify-content:center;background:rgba(255,255,255,.06)}
.service svg{width:56px;height:56px;fill:var(--white)}

/* blog + testimonials */
.lower{position:absolute;left:0;top:1480px;width:1200px;height:300px}
.col-head{position:absolute;top:0;display:flex;align-items:center;gap:10px;font-size:24px;font-weight:800;color:var(--ink)}
.col-head b{color:var(--blue)}
.col-head svg{width:28px;height:28px;fill:var(--blue)}
.arrows{position:absolute;top:6px;font-size:20px;color:var(--muted);letter-spacing:12px}
.blog{position:absolute;left:120px;top:54px;width:470px}
.post{display:flex;gap:14px;margin-bottom:16px}
.thumb{width:62px;height:62px;flex:none;background:linear-gradient(135deg,#8a7866,#4a4038)}
.post h4{font-size:13px;font-weight:700;color:var(--ink);display:flex;justify-content:space-between}
.post h4 span{font-weight:600;color:var(--muted);font-size:12px}
.post p{font-size:12px;line-height:1.5;color:#777;margin-top:3px}
.quote{position:absolute;left:630px;top:54px;width:450px;height:140px;border:2px solid #d4d6d9;border-radius:14px;padding:18px 22px;font-size:13px;line-height:1.6;color:#666}
.quote:after{content:"";position:absolute;left:60px;bottom:-14px;width:24px;height:24px;background:var(--white);border-right:2px solid #d4d6d9;border-bottom:2px solid #d4d6d9;transform:rotate(45deg)}
.client{position:absolute;left:650px;top:212px;display:flex;align-items:center;gap:14px;font-size:14px;color:var(--ink)}
.avatar{width:64px;height:64px;border-radius:50%;background:linear-gradient(135deg,#9a8674,#5a4c40);border:3px solid #ddd}

/* contact */
.contact{position:absolute;left:0;top:1780px;width:1200px;height:412px;background:linear-gradient(160deg,#6a6d6f,#44474a)}
.contact .map{position:absolute;inset:0;background:radial-gradient(ellipse at 80% 60%,rgba(120,125,128,.45),rgba(0,0,0,0) 60%)}
.panel-title{position:absolute;top:0;height:52px;width:480px;background:rgba(30,32,36,.55);color:var(--white);font-size:22px;font-weight:600;letter-spacing:1px;padding:12px 16px;text-transform:uppercase}
.inquiry{position:absolute;left:120px;top:0;width:480px;height:412px;background:rgba(30,32,36,.45)}
.inquiry .panel-title{left:0}
.inquiry p{position:absolute;left:16px;top:70px;width:440px;font-size:13px;color:#ddd;line-height:1.5}
.field{position:absolute;left:16px;width:440px;height:32px;background:var(--white);font-size:12px;color:#999;padding:7px 10px}
.submit{position:absolute;left:356px;top:336px;width:100px;height:34px;background:#1b1d21;color:var(--white);font-size:14px;font-weight:800;letter-spacing:1px;display:flex;align-items:center;justify-content:center}
.info{position:absolute;left:620px;top:0;width:480px;height:412px}
.info .panel-title{left:0;background:rgba(30,32,36,.55)}
.info-row{position:absolute;left:16px;display:flex;align-items:center;gap:16px;color:var(--white);font-size:15px;font-weight:600;line-height:1.5}
.info-row .ico{width:40px;height:40px;border-radius:50%;background:#2a2c30;display:flex;align-items:center;justify-content:center;flex:none}
.info-row svg{width:20px;height:20px;fill:var(--white)}

/* footer */
.footer{position:absolute;left:0;top:2192px;width:1200px;height:164px;background:#1f2124}
.footer-nav{position:absolute;left:0;top:34px;width:1200px;display:flex;justify-content:center;gap:0}
.footer-nav a{color:#ccc;text-decoration:none;font-size:14px;padding:0 16px;border-right:1px solid #555}
.footer-nav a:last-child{border-right:none}
.footer-line{position:absolute;left:120px;top:80px;width:960px;height:1px;background:#3a3c40}
.copyright{position:absolute;left:136px;top:106px;font-size:13px;color:#aaa}
.footer .social{position:absolute;right:120px;top:100px}
</style>
</head>
<body>
<div class="page">

  <section class="hero">
    <div class="hero-art" role="img" aria-label="Businessman touching a glowing grid of cloud and data icons"></div>
    <div class="topbar"></div>
    <div class="brand"><span class="brand-mark"></span><span class="brand-name">KR SOLUTIONS GROUP</span></div>
    <div class="phone">
      <svg width="18" height="18" viewBox="0 0 24 24" fill="#fff"><path d="M6.6 10.8a15 15 0 0 0 6.6 6.6l2.2-2.2a1 1 0 0 1 1-.25 11.4 11.4 0 0 0 3.6.6 1 1 0 0 1 1 1V20a1 1 0 0 1-1 1A17 17 0 0 1 3 4a1 1 0 0 1 1-1h3.5a1 1 0 0 1 1 1c0 1.25.2 2.45.6 3.6a1 1 0 0 1-.25 1z"/></svg>
      1300 555 019
    </div>
    <div class="social"><span></span><span></span><span></span><span></span></div>
    <h1 class="hero-title">Managed IT Services &amp;<br>A Resilient Cloud Platform<br>For The SMB Sector</h1>
    <div class="dots"><i></i><i></i><i></i></div>
  </section>

  <nav class="nav">
    <a href="#"><svg viewBox="0 0 24 24"><path d="M12 3l10 9h-3v9h-5v-6h-4v6H5v-9H2z"/></svg>Home</a>
    <a href="#"><svg viewBox="0 0 24 24"><circle cx="12" cy="7" r="4"/><path d="M4 21c0-4.4 3.6-8 8-8s8 3.6 8 8z"/></svg>Consult</a>
    <a href="#"><svg viewBox="0 0 24 24"><path d="M3 4h3l3 11h10l2-8H8"/><circle cx="10" cy="19" r="2"/><circle cx="17" cy="19" r="2"/></svg>Procure</a>
    <a href="#"><svg viewBox="0 0 24 24"><path d="M12 2l3 7h7l-5.5 4.5 2 7.5L12 16.5 5.5 21l2-7.5L2 9h7z"/></svg>Provision</a>
    <a href="#"><svg viewBox="0 0 24 24"><path d="M6 19a5 5 0 0 1-.5-10A6.5 6.5 0 0 1 18 8a4.5 4.5 0 0 1 0 11z"/></svg>Cloud &amp; Connectivity</a>
    <a href="#"><svg viewBox="0 0 24 24"><path d="M2 4h20v13H2zM8 20h8v2H8z"/></svg>Software Development</a>
    <a href="#"><svg viewBox="0 0 24 24"><path d="M4 3h16v14H9l-5 4z"/></svg>Blog</a>
    <a href="#"><svg viewBox="0 0 24 24"><path d="M2 5h20v14H2zM2 5l10 8 10-8"/></svg>Contact Us</a>
  </nav>

  <section class="about">
    <div class="about-mark"></div>
    <h2>ABOUT <b>K &amp; R SOLUTIONS GROUP</b></h2>
    <p>We help small and medium businesses plan, buy and run the technology they depend on every day. Our team consults on strategy, procures the right hardware and licences, provisions secure systems and supports them long after go-live. From cloud hosting and connectivity to custom software, we act as one accountable partner so your staff can focus on customers instead of servers. We work with clear pricing, fast response times and plain language, and we measure success by how smoothly your business runs, not by how many tickets we close each month.</p>
    <span class="read-more">Read More &#9654;</span>
  </section>

  <section class="services">
    <svg class="bg" width="1200" height="410" viewBox="0 0 1200 410"><polygon points="0,30 1200,0 1200,380 0,410" fill="#2d2f33"/></svg>
    <p class="services-intro">IN ADDITION TO OUR PROCUREMENT SERVICES, KRSG IS AN INDUSTRY LEADER IN THE DELIVERY OF THE FOLLOWING IT SERVICES:</p>
    <div class="service-list">
      <div class="service"><div class="ring"><svg viewBox="0 0 24 24"><circle cx="12" cy="6" r="3"/><circle cx="5" cy="11" r="2.4"/><circle cx="19" cy="11" r="2.4"/><path d="M7 20c0-3 2.2-6 5-6s5 3 5 6zM1 19c0-2.5 1.8-5 4-5 1 0 1.8.4 2.4 1-1 1.2-1.4 2.6-1.4 4zM23 19c0-2.5-1.8-5-4-5-1 0-1.8.4-2.4 1 1 1.2 1.4 2.6 1.4 4z"/></svg></div>TECHNOLOGY<br>CONSULTING</div>
      <div class="service"><div class="ring"><svg viewBox="0 0 24 24"><rect x="9" y="2" width="6" height="5"/><rect x="2" y="17" width="6" height="5"/><rect x="16" y="17" width="6" height="5"/><path d="M11.3 7h1.4v4H20v6h-1.4v-4.6H5.4V17H4v-6h7.3z"/></svg></div>MANAGED IT<br>SERVICES</div>
      <div class="service"><div class="ring"><svg viewBox="0 0 24 24"><path d="M6 15a4.5 4.5 0 0 1-.4-9A6 6 0 0 1 17 5.5a4 4 0 0 1 .5 9.5zM11.3 15h1.4v3H20v1.4h-7.3V22h-1.4v-2.6H4V18h7.3z"/></svg></div>CLOUD SERVICES &amp;<br>HOSTING</div>
      <div class="service"><div class="ring"><svg viewBox="0 0 24 24"><path d="M2 3h20v14H2zm2 2v10h16V5zM8 20h8v2H8zM10 17h4v3h-4zM6 13l4-5 3 3 2-2 3 4z"/></svg></div>SOFTWARE<br>DEVELOPMENT</div>
    </div>
  </section>

  <section class="lower">
    <div class="col-head" style="left:120px"><svg viewBox="0 0 24 24"><path d="M4 3h16v18H4zM7 7h10v2H7zm0 4h10v2H7zm0 4h6v2H7z" fill-rule="evenodd"/></svg><span><b>LATEST</b> BLOG</span></div>
    <div class="arrows" style="left:540px">&#8249;&#8250;</div>
    <div class="blog">
      <div class="post"><div class="thumb" role="img" aria-label="Portrait photo of the post author"></div><div><h4>Lorem ipsum dolor sit amet Lorem <span>05AUG, 2013</span></h4><p>Short update on cloud backups, new support hours and practical tips for keeping office systems secure.</p></div></div>
      <div class="post"><div class="thumb" role="img" aria-label="Portrait photo of the post author"></div><div><h4>Lorem ipsum dolor sit amet Lorem <span>05AUG, 2013</span></h4><p>Short update on cloud backups, new support hours and practical tips for keeping office systems secure.</p></div></div>
      <div class="post"><div class="thumb" role="img" aria-label="Portrait photo of the post author"></div><div><h4>Lorem ipsum dolor sit amet Lorem <span>05AUG, 2013</span></h4><p>Short update on cloud backups, new support hours and practical tips for keeping office systems secure.</p></div></div>
    </div>

    <div class="col-head" style="left:630px"><svg viewBox="0 0 24 24"><path d="M3 4h18v12H10l-5 4v-4H3z"/></svg><span><b>CLIENT</b> TESTIMONIALS</span></div>
    <div class="arrows" style="left:1040px">&#8249;&#8250;</div>
    <div class="quote">Moving our whole office to their managed platform was the easiest upgrade we have made. Response times are quick, the team explains things clearly and our systems simply work. We now plan our growth knowing our technology will keep pace with us.</div>
    <div class="client"><div class="avatar" role="img" aria-label="Client portrait photo"></div>Mr Owen Hartley</div>
  </section>

  <section class="contact">
    <div class="map" role="img" aria-label="Street map of the office location"></div>
    <div class="inquiry">
      <div class="panel-title">Quick Inquiry</div>
      <p>Send us a short note and a member of our team will reply within one business day.</p>
      <div class="field" style="top:130px">First Name</div>
      <div class="field" style="top:178px">Last Name</div>
      <div class="field" style="top:226px">Email</div>
      <div class="field" style="top:274px">Phone</div>
      <div class="submit">SUBMIT</div>
    </div>
    <div class="info">
      <div class="panel-title">Contact Info</div>
      <div class="info-row" style="top:80px"><span class="ico"><svg viewBox="0 0 24 24"><path d="M12 2a7 7 0 0 0-7 7c0 5 7 13 7 13s7-8 7-13a7 7 0 0 0-7-7zm0 9.5A2.5 2.5 0 1 1 12 6.5a2.5 2.5 0 0 1 0 5z"/></svg></span><span>Level 4, 12 Harbour Lane<br>Northgate, Queensland 4100</span></div>
      <div class="info-row" style="top:170px"><span class="ico"><svg viewBox="0 0 24 24"><path d="M6.6 10.8a15 15 0 0 0 6.6 6.6l2.2-2.2a1 1 0 0 1 1-.25 11.4 11.4 0 0 0 3.6.6 1 1 0 0 1 1 1V20a1 1 0 0 1-1 1A17 17 0 0 1 3 4a1 1 0 0 1 1-1h3.5a1 1 0 0 1 1 1c0 1.25.2 2.45.6 3.6a1 1 0 0 1-.25 1z"/></svg></span><span>1300 555 019</span></div>
      <div class="info-row" style="top:240px"><span class="ico"><svg viewBox="0 0 24 24"><path d="M2 5h20v14H2zm2 2v.5l8 6 8-6V7z"/></svg></span><span>hello@krsolutions.example</span></div>
    </div>
  </section>

  <footer class="footer">
    <nav class="footer-nav">
      <a href="#">Home</a><a href="#">Consult</a><a href="#">Procure</a><a href="#">Provision</a><a href="#">Cloud &amp; Connectivity</a><a href="#">Software Development</a><a href="#">Blog</a><a href="#">Contact Us</a>
    </nav>
    <div class="footer-line"></div>
    <p class="copyright">&copy; 2013 K &amp; R Solutions Group . All Rights Reserved</p>
    <div class="social"><span></span><span></span><span></span><span></span></div>
  </footer>

</div>
</body>
</html>
```